Organic Sunscreen Business "VelloBloom" Needs Package Design

Our company VelloBloom, manufactures an anti-ageing SPF 15 sunscreen product.

We specialise in the world's most rare and luxury organic anti-ageing ingredients.

We require an attractive package design for a 2.5 oz/75 ml squeezy bottle with box design, a few examples of similar examples which we like are attached.

We have a logo, barcode and graphic, which has been uploaded, and the bottle is to convey the message of wealth and luxury as well as organic sunscreen, we would prefer the package to be colourful and creative in order to sell.

I have included 2 rough sketches of the basic elements and layout of the design. And the box is to be similar to the bottle but to contain an extra caption.

Also, the sketch is only for a guide on how I would like the package, i.e. the labels and graphics can be in different positions/layouts thanks. And any additional creative images, text or fonts would be considered.
Updates

Industry/Entity Type

Business

Requirements
Must have
• FRONT of Bottle:
• LABEL 1: Logo (attached)
• LABEL 2:
• SPF 15
• Non-Nano
• Technology
• 100% Organic
• Paraben Free
• LABEL 3: (Larger/higher emphasis than Label 2)
• Anti-Ageing
• Moisturiser
• BACK of Bottle:
• Introduction: (For me to add personally at later date)
• Warnings: For external use only. Do not use on damaged or broken skin. Stop use and ask a doctor if rash occurs. When using this product keep out of eyes. Rinse with water to remove.
• Directions: Shake well before use. Apply liberally 15 minutes before sun exposure. Use a water resistant sunscreen if swimming or sweating. Reapply at least every 2 hours. Children under 6 months: Ask a doctor.
• Active Ingredient: Non-Nano Zinc Oxide (6%)
• Also contains: (For me to add personally at later date)
• Barcode: (image attached)
• Contact: www.vellobloom-example.com.au
• 2.5oz/7ml e
• BOX:
• Same as bottle, but one side will contain the caption:
• "7 NATURAL WONDERS IN 1" (In a creative style)
Nice to have
• Additional Text/Images/Fonts relating to the subject(s)
• Most creative design will be the winner.

```html
<!DOCTYPE html>
<html lang="en">
<head>
<meta charset="utf-8">
<title>VelloBloom Anti-Ageing Moisturiser Packaging</title>
<link rel="stylesheet" href="https://fonts.googleapis.com/css2?family=Cinzel:wght@400;500&display=swap">
<style>
  :root {
    --bg: #ececec;
    --panel-dark: #3a3937;
    --panel-side: #2e2d2b;
    --tube-dark: #38342c;
    --text-light: #ecebe8;
    --gold: #c9a227;
    --gold-light: #e8c95a;
    --gold-dark: #8a6a12;
    --cap: #2a2a2a;
    --scene-sky: #9a9a9a;
    --scene-sand: #d9d9d9;
  }
  * { box-sizing: border-box; margin: 0; padding: 0; }
  html, body { width: 1200px; height: 938px; overflow: hidden; }
  body {
    background: var(--bg);
    font-family: "Cinzel", serif;
    color: var(--text-light);
    position: relative;
  }
  .box-side {
    position: absolute; left: 200px; top: 110px; width: 170px; height: 700px;
    background: var(--panel-side);
    display: flex; flex-direction: column; align-items: center; justify-content: center;
    text-align: center;
  }
  .caption-number { font-size: 70px; line-height: 1; margin: 10px 0; }
  .caption-words { font-size: 28px; line-height: 1.25; }
  .box-front, .tube-label {
    position: absolute; display: flex; flex-direction: column; align-items: center; text-align: center;
  }
  .box-front { left: 370px; top: 110px; width: 235px; height: 700px; background: var(--panel-dark); }
  .scene-art {
    width: 100%;
    background: linear-gradient(to bottom, var(--scene-sky) 0%, #c8c8c8 55%, var(--scene-sand) 60%, #eeeeee 100%);
  }
  .box-front .scene-art { height: 190px; }
  .product-title { font-size: 29px; line-height: 1.1; margin-top: 14px; letter-spacing: 0.5px; }
  .rule { width: 100%; height: 2px; background: #cfcfcf; margin: 10px 0 8px; }
  .claims { font-size: 12px; letter-spacing: 0.5px; }
  .spf-badge {
    margin-top: 80px; padding: 2px 10px;
    background: linear-gradient(135deg, var(--gold-dark), var(--gold-light) 45%, var(--gold) 70%, var(--gold-dark));
    color: #2b2510; font-size: 34px; line-height: 1.2;
  }
  .tech { color: var(--gold); font-size: 13px; margin-top: 4px; }
  .brand { margin-top: 70px; display: flex; flex-direction: column; align-items: center; gap: 12px; }
  .brand-dot { width: 60px; height: 60px; border-radius: 50%; background: var(--gold); }
  .brand-name { font-size: 20px; color: var(--text-light); }
  .volume { font-size: 18px; margin-top: 30px; }
  .tube {
    position: absolute; left: 640px; top: 150px; width: 370px; height: 630px;
    clip-path: polygon(0 0, 100% 0, 90% 100%, 10% 100%);
    background: var(--tube-dark);
  }
  .tube-label { inset: 0; }
  .tube .scene-art { height: 200px; }
  .tube .product-title { font-size: 30px; margin-top: 16px; }
  .tube .claims { font-size: 15px; }
  .tube .spf-badge { margin-top: 55px; font-size: 36px; }
  .tube .brand { margin-top: 40px; }
  .tube .volume { margin-top: 22px; }
  .tube-cap {
    position: absolute; left: 677px; top: 780px; width: 296px; height: 120px;
    background: var(--cap); border-radius: 0 0 18px 18px;
  }
</style>
</head>
<body>
  <section class="box-side">
    <div class="caption-number">7</div>
    <div class="caption-words">Natural<br>Wonders<br>In</div>
    <div class="caption-number">1</div>
  </section>

  <section class="box-front">
    <div class="scene-art" role="img" aria-label="Black and white photograph of the pyramids in the desert under a cloudy sky"></div>
    <h1 class="product-title">Anti-Ageing<br>Moisturiser</h1>
    <div class="rule"></div>
    <p class="claims">100% Organic - Paraben Free</p>
    <div class="spf-badge">SPF 15</div>
    <p class="tech">Non-Nano Technology</p>
    <div class="brand"><span class="brand-dot"></span><span class="brand-name">VelloBloom</span></div>
    <p class="volume">2.5oz/75ml e</p>
  </section>

  <section class="tube">
    <div class="tube-label">
      <div class="scene-art" role="img" aria-label="Black and white photograph of the pyramids in the desert under a cloudy sky"></div>
      <h2 class="product-title">Anti-Ageing<br>Moisturiser</h2>
      <div class="rule"></div>
      <p class="claims">100% Organic - Paraben Free</p>
      <div class="spf-badge">SPF 15</div>
      <p class="tech">Non-Nano Technology</p>
      <div class="brand"><span class="brand-dot"></span><span class="brand-name">VelloBloom</span></div>
      <p class="volume">2.5oz/75ml e</p>
    </div>
  </section>
  <div class="tube-cap"></div>
</body>
</html>
```